Website redesign for a Cloud Advisory business

We are looking to revisit our existing brand and website, with a view to updating both. Looking for concepts and designs for how the website might look, flow and feel. Current website is: www.brellomint.com.au

Scope and Deliverables: Concept design for the home page and one internal page.

We do not expect you to design all the pages and all the elements of the website at this stage.

This job is not for the full website design, but just for concepts that we can start with when we go into the full website design.

We would love to see a design feature based on our name, logo, or industry, which can run through banners and other collateral (twitter banner, ads on Google, corporate documents etc).

We want the brand to properly depict what we bring/deliver to businesses when consulting to them and this should extend to the colour scheme, logo, font (perhaps updated) and copy (which will be supplied).

Our brand should suitably communicate our ability, knowledge and extensive experience within the Cloud space.

It should express and evoke credibility, knowledge and understanding of the Cloud space, independence, gravitas, reliability, efficiency, trust, expertise, approachability, service delivery but be uncomplicated, practical and use plain speaking language.

Colours that reinforce this might include: Blues, blacks, silver, white, grey and our existing orange.

Website designs that we like or have referenced include:

Varnolift: http://varnolift.com.au/ - This has good information but looks a little amateur in it’s cartoon like design and colour scheme. Also, this seems to be aimed at clients more interested in price than design and what we are going for is a little more high end.

Pendramoor: https://www.pendramoor.com.au/ - This site has merit in its’ setup but little call to action on the home page, especially before the scroll line. I like the set up of the Case Studies page however I’d look to make it more prominent by having it set up 3 across rather than the 4 they have. Something such as this: https://www.qandelby.com/case-studies

Tolvane: http://www.tolvane.com.au/#home4 - This page is a good one as far as selling services and information on the company. I quite like it.

MirefoldIT: http://www.mirefoldit.com.au/ - While I don’t think is particularly creative, it does practically depict the services we offer in a fairly clear way and might be a bit of a basic (albeit dull) template to follow.

JDP: https://store.jdp.com/us/Product-Family/JDP-Advisory-Services/JDP-Cloud-Advisory-Service/p/JDP-Services-Cloud-Advisory - This offers substantial information but is probably a little confusing although the roll-over drop down menus have merit.

ZEV: http://www.zev.net.au/en/services/ - While this in not quite what we are looking for, the colour scheme gives it more gravitas and quality.

As another reference, this website and the way they present their case studies is also something we like, although I’d like them shown 3 up, side by side…. https://www.qandelby.com/case-studies.

We have added a page layout and page purpose document.

Target Market(s)

Corporates, small - medium business, direct referrals, via search results

Industry/Entity Type

Business

Number of Pages Required

1 page

Font styles to use
Sans Serif

Colors
85abd2
0455a3
000000
f37122
5c5c5c

Requirements
Must have
• Website must be mobile device compatible.
• Concept design for the home page.
Nice to have
• We would love to see a design feature based on our name, logo, or industry, which can run through banners and other collateral (twitter banner, ads on Google, corporate documents etc).

```html
<!DOCTYPE html>
<html lang="en">
<head>
<meta charset="utf-8">
<title>Brellomint — Impartial Cloud Solutions</title>
<link href="https://fonts.googleapis.com/css2?family=Roboto:wght@300;400;500;700;900&display=swap" rel="stylesheet">
<style>
:root{
  --orange:#f37122;
  --ink:#1f1f1f;
  --dark:#2b2b30;
  --darker:#1b1b1e;
  --grey:#5c5c5c;
  --light:#9a9a9a;
  --line:#e2e2e2;
  --white:#ffffff;
  --blue:#0455a3;
  --sky:#85abd2;
}
*{box-sizing:border-box;margin:0;padding:0}
html,body{width:1200px;height:3757px;overflow:hidden}
body{font-family:'Roboto',sans-serif;color:var(--grey);background:var(--white);position:relative}
.abs{position:absolute}
h2.section-title{position:absolute;left:0;width:1200px;text-align:center;font-size:34px;font-weight:500;color:var(--ink)}
h2.section-title::after{content:"";display:block;width:46px;height:3px;background:var(--orange);margin:12px auto 0}

/* header */
.topbar{left:0;top:0;width:1200px;height:96px;background:var(--darker)}
.brand{left:70px;top:20px;display:flex;align-items:center;gap:10px}
.brand-mark{width:22px;height:22px;background:var(--orange)}
.brand-name{font-size:28px;font-weight:700;color:var(--white);letter-spacing:1px}
.contact-line{right:70px;top:30px;display:flex;gap:22px;align-items:center;font-size:13px;color:#cfcfcf}
.socials{display:flex;gap:8px}
.socials i{width:14px;height:14px;border-radius:50%;background:#8a8a8a;display:block}
.nav{left:0;top:96px;width:1200px;height:40px;background:rgba(20,20,22,.85);z-index:2}
.nav ul{list-style:none;display:flex;gap:26px;position:absolute;left:70px;top:12px;font-size:13px;color:#e8e8e8}
.nav .search{right:72px;top:12px;width:14px;height:14px}

/* hero */
.hero{left:0;top:96px;width:1200px;height:624px;background:linear-gradient(180deg,#8f8b86 0%,#b9b3ab 45%,#6e6a66 100%)}
.hero-shade{left:0;top:96px;width:1200px;height:624px;background:linear-gradient(180deg,rgba(0,0,0,.15),rgba(0,0,0,.35))}
.hero h1{left:0;top:352px;width:1200px;text-align:center;color:var(--white);font-size:52px;font-weight:700;letter-spacing:.5px}
.hero-sub{left:0;top:448px;width:1200px;text-align:center;color:var(--white);font-size:27px;font-weight:300;line-height:40px}
.btn{display:inline-block;background:var(--orange);color:var(--white);font-weight:500;text-transform:uppercase;font-size:15px}
.hero-btn{left:470px;top:556px;width:260px;height:56px;line-height:56px;text-align:center}
.hero-arrow{top:380px;width:26px;height:54px;background:rgba(255,255,255,.25)}

/* services */
.services-title{top:770px}
.svc-arrow{top:930px;width:34px;height:34px;display:flex;align-items:center;justify-content:center}
.svc-list{left:135px;top:862px;width:930px;display:grid;grid-template-columns:repeat(4,1fr);gap:20px}
.svc{text-align:center}
.svc-icon{width:60px;height:60px;border:2px solid var(--orange);border-radius:50%;margin:0 auto 16px;display:flex;align-items:center;justify-content:center}
.svc h3{font-size:15px;font-weight:700;color:var(--ink);margin-bottom:8px;line-height:19px}
.svc p{font-size:11px;line-height:16px;color:var(--light)}

/* who we are */
.who-photo{left:0;top:1110px;width:600px;height:490px;background:linear-gradient(135deg,#c7ccd3,#8c96a3 55%,#4c5460)}
.who-panel{left:600px;top:1110px;width:600px;height:490px;background:var(--dark)}
.who-panel h2{position:absolute;left:60px;top:52px;font-size:38px;font-weight:500;color:var(--white)}
.who-panel h2 span{color:var(--orange)}
.who-panel .rule{left:60px;top:108px;width:44px;height:3px;background:var(--orange)}
.who-panel p{position:absolute;left:60px;width:470px;font-size:12.5px;line-height:19px;color:#bdbdbd}
.read-more{left:60px;top:358px;width:120px;height:36px;border:1px solid #9a9a9a;color:var(--white);font-size:11px;text-align:center;line-height:34px;letter-spacing:1px}
.who-feats{left:60px;top:426px;display:flex;gap:40px}
.feat{display:flex;align-items:center;gap:10px;color:var(--white);font-size:14px;line-height:16px}
.feat svg{flex:none}

/* testimonials + values */
.t-title{left:70px;top:1680px;font-size:26px;font-weight:500;color:var(--ink)}
.small-rule{width:40px;height:3px;background:var(--orange)}
.t-avatar{left:74px;top:1740px;width:80px;height:80px;border-radius:50%;background:linear-gradient(160deg,#c9b8a6,#6d625a)}
.t-head{left:170px;top:1752px;font-size:17px;font-weight:500;color:var(--ink)}
.t-meta{left:170px;top:1780px;font-size:11px;color:var(--light)}
.stars{left:170px;top:1800px;color:var(--orange);font-size:14px;letter-spacing:3px}
.t-quote{left:70px;top:1842px;width:360px;font-size:12px;line-height:19px;color:var(--light)}
.dots{left:240px;top:2030px;display:flex;gap:8px}
.dots i{width:9px;height:9px;border-radius:50%;background:#cfcfcf;display:block}
.dots i.on{background:var(--orange)}
.v-title{left:505px;top:1680px;font-size:26px;font-weight:500;color:var(--ink)}
.tabs{left:505px;top:1756px;width:625px;height:36px;display:flex;border:1px solid var(--line)}
.tabs div{flex:1;text-align:center;line-height:34px;font-size:13px;color:var(--grey)}
.tabs div.on{background:var(--orange);color:var(--white)}
.v-sub{left:505px;top:1826px;font-size:14px;font-weight:700;color:var(--ink)}
.v-text{left:505px;top:1852px;width:625px;font-size:11.5px;line-height:18px;color:var(--light)}
.v-device{left:870px;top:1900px;width:250px;height:110px;background:linear-gradient(160deg,#f2f2f2,#c9c9c9)}
.checklist{list-style:none;font-size:12px;color:var(--grey)}
.checklist li{display:flex;align-items:center;gap:8px;height:26px}
.tick{width:10px;height:10px;flex:none}

/* helping */
.help-band{left:0;top:2107px;width:1200px;height:290px;background:var(--darker)}
.help-photo{left:0;top:2107px;width:520px;height:290px;background:linear-gradient(140deg,#6e6a66,#b3aca3 55%,#3b3a3c)}
.help-frame{left:30px;top:2125px;width:490px;height:254px;border:2px solid rgba(255,255,255,.85)}
.help-title{left:583px;top:2150px;font-size:20px;font-weight:700;color:var(--white)}
.help-text{left:583px;top:2185px;width:520px;font-size:12px;line-height:18px;color:#bdbdbd}
.help-list{color:#e4e4e4}

/* stats */
.stats{left:0;top:2405px;width:1200px;height:162px;background:var(--orange)}
.stat{position:absolute;top:48px;display:flex;align-items:center;gap:14px;color:var(--white)}
.stat b{font-size:60px;font-weight:500;line-height:60px}
.stat span{font-size:15px;font-weight:500;line-height:19px;text-transform:uppercase}

/* team */
.team-title{top:2626px}
.team{left:123px;top:2727px;display:grid;grid-template-columns:repeat(4,230px);gap:20px}
.member-photo{height:230px}
.member-tag{height:72px;background:var(--darker);text-align:center;padding-top:16px}
.member-tag h4{font-size:16px;font-weight:700;color:var(--orange)}
.member-tag p{font-size:11px;color:#cfcfcf;margin-top:6px}

/* cta */
.cta{left:0;top:3090px;width:1200px;height:90px;background:var(--orange)}
.cta p{position:absolute;left:138px;top:30px;font-size:25px;color:var(--white);font-weight:500}
.cta .btn-cta{left:890px;top:28px;width:160px;height:36px;background:var(--darker);color:var(--white);font-size:13px;font-weight:500;display:flex;align-items:center;justify-content:center;gap:12px}
.cta .btn-cta i{width:18px;height:18px;border-radius:50%;background:var(--white);display:block}

/* contact */
.contact{left:0;top:3180px;width:1200px;height:516px;background:linear-gradient(180deg,#232326,#1c1c1f)}
.contact-map{left:120px;top:3180px;width:1000px;height:500px;background:radial-gradient(ellipse at center,rgba(255,255,255,.06),rgba(255,255,255,0) 70%)}
.contact h2{position:absolute;left:0;top:60px;width:1200px;text-align:center;font-size:34px;font-weight:500;color:var(--white)}
.contact h2::after{content:"";display:block;width:46px;height:3px;background:var(--orange);margin:12px auto 0}
.field{position:absolute;left:198px;width:394px;height:50px;background:var(--white);font-size:11px;color:#a5a5a5;padding:16px 14px}
.field.area{left:614px;top:3355px;width:394px;height:178px}
.send{left:500px;top:3568px;width:200px;height:48px;line-height:48px;text-align:center}

/* footer */
.footer{left:0;top:3696px;width:1200px;height:61px;background:var(--darker);border-top:1px solid #333}
.footer p{position:absolute;left:122px;top:22px;font-size:12px;color:#8b8b8b}
.footer .fsocial{right:120px;top:14px;display:flex;gap:10px}
.footer .fsocial i{width:32px;height:32px;border-radius:50%;background:#3a3a3e;display:block}
</style>
</head>
<body>

<header>
  <div class="abs topbar"></div>
  <div class="abs brand"><span class="brand-mark"></span><span class="brand-name">BRELLOMINT</span></div>
  <div class="abs contact-line">
    <span>1300 555 014</span>
    <div class="socials"><i></i><i></i><i></i><i></i></div>
    <span>info@brellomint.com.au</span>
  </div>
  <nav class="abs nav">
    <ul><li>Home</li><li>About Us</li><li>Advisory Specialties</li><li>Services</li><li>The Company We Keep</li><li>Case Studies and Testimonials</li><li>FAQ's</li><li>Blog</li><li>Resources and Links</li><li>Contact Us</li></ul>
    <svg class="abs search" viewBox="0 0 14 14"><circle cx="6" cy="6" r="4.5" fill="none" stroke="#e8e8e8" stroke-width="1.6"/><line x1="9.5" y1="9.5" x2="13" y2="13" stroke="#e8e8e8" stroke-width="1.6"/></svg>
  </nav>
</header>

<section>
  <div class="abs hero" role="img" aria-label="Group of smiling business people in suits gathered around a laptop"></div>
  <div class="abs hero-shade"></div>
  <div class="abs hero-arrow" style="left:0"></div>
  <div class="abs hero-arrow" style="right:0"></div>
  <div class="hero">
    <h1 class="abs hero" style="background:none;height:auto;top:352px">IMPARTIAL CLOUD SOLUTIONS</h1>
  </div>
  <p class="abs hero-sub">We provide impartial advice on cloud solutions ensuring<br>it's always right for you.</p>
  <a class="abs btn hero-btn">Book a free consultation</a>
</section>

<section>
  <h2 class="section-title services-title">Our Services</h2>
  <div class="abs svc-arrow" style="left:72px;background:#d8d8d8">
    <svg width="10" height="14" viewBox="0 0 10 14"><path d="M8 1 2 7l6 6" fill="none" stroke="#fff" stroke-width="2"/></svg>
  </div>
  <div class="abs svc-arrow" style="left:1094px;background:var(--orange)">
    <svg width="10" height="14" viewBox="0 0 10 14"><path d="M2 1l6 6-6 6" fill="none" stroke="#fff" stroke-width="2"/></svg>
  </div>
  <div class="abs svc-list">
    <div class="svc">
      <div class="svc-icon"><svg width="26" height="26" viewBox="0 0 26 26"><path d="M9 4v10l-3-2-2 2 7 8h9l2-9-8-2V4z" fill="none" stroke="#f37122" stroke-width="2"/></svg></div>
      <h3>System Selection</h3>
      <p>Find the right system for you. Online or cloud based, covering finance, stock and the tools your team uses day to day.</p>
    </div>
    <div class="svc">
      <div class="svc-icon"><svg width="26" height="26" viewBox="0 0 26 26"><circle cx="13" cy="13" r="6" fill="none" stroke="#f37122" stroke-width="2"/><circle cx="13" cy="13" r="10.5" fill="none" stroke="#f37122" stroke-width="2" stroke-dasharray="4 3"/></svg></div>
      <h3>Accounting Systems &amp;<br>Conversions</h3>
      <p>Convert your ledgers and history into a modern cloud package with clean data and simple reports.</p>
    </div>
    <div class="svc">
      <div class="svc-icon"><svg width="28" height="24" viewBox="0 0 28 24"><rect x="2" y="2" width="24" height="15" fill="none" stroke="#f37122" stroke-width="2"/><path d="M10 22h8M14 17v5" stroke="#f37122" stroke-width="2"/></svg></div>
      <h3>Integration</h3>
      <p>Link your existing apps so data moves between them, making a single source of truth across the business.</p>
    </div>
    <div class="svc">
      <div class="svc-icon"><svg width="26" height="26" viewBox="0 0 26 26"><rect x="4" y="4" width="18" height="18" fill="none" stroke="#f37122" stroke-width="2"/><path d="M4 10h18M10 10v12" stroke="#f37122" stroke-width="2"/></svg></div>
      <h3>Business Inventory</h3>
      <p>Get started with the right inventory system for stock, orders and dispatch, linked to your ledger.</p>
    </div>
  </div>
</section>

<section>
  <div class="abs who-photo" role="img" aria-label="Confident businessman in a suit with colleagues behind him in an office"></div>
  <div class="abs who-panel">
    <h2>Who We <span>Are</span></h2>
    <div class="abs rule"></div>
    <p style="top:130px">Lorem Ipsum is simply dummy text of the printing and typesetting industry. Lorem Ipsum has been the industry's standard dummy text ever since the 1500s, when an unknown printer took a galley of type and scrambled it to make a type specimen book. It has survived not only five centuries.</p>
    <p style="top:238px">It has also seen the leap into electronic typesetting, remaining essentially unchanged. It was popularised in the 1960s with the release of sheets containing passages, and more recently with desktop publishing software like page makers including versions of Lorem Ipsum.</p>
    <div class="abs read-more">READ MORE</div>
    <div class="abs who-feats">
      <div class="feat"><svg width="30" height="30" viewBox="0 0 30 30"><circle cx="10" cy="10" r="4" fill="#f37122"/><circle cx="20" cy="10" r="4" fill="#f37122"/><path d="M2 26c0-6 4-9 8-9s8 3 8 9zM12 26c0-6 4-9 8-9s8 3 8 9z" fill="#f37122"/></svg><span>Dedicated<br>Team</span></div>
      <div class="feat"><svg width="30" height="30" viewBox="0 0 30 30"><circle cx="15" cy="12" r="9" fill="none" stroke="#f37122" stroke-width="2.5"/><path d="M10 20l-3 8 8-4 8 4-3-8" fill="#f37122"/></svg><span>Best<br>Advisors</span></div>
      <div class="feat"><svg width="30" height="30" viewBox="0 0 30 30"><circle cx="15" cy="15" r="12" fill="none" stroke="#f37122" stroke-width="2.5"/><path d="M15 8v7l5 3" fill="none" stroke="#f37122" stroke-width="2.5"/></svg><span>24/7<br>Supports</span></div>
    </div>
  </div>
</section>

<section>
  <h2 class="abs t-title">Testimonials</h2>
  <div class="abs small-rule" style="left:70px;top:1722px"></div>
  <div class="abs t-avatar" role="img" aria-label="Portrait of a client"></div>
  <div class="abs t-head">Quenfield is Great Firm</div>
  <div class="abs t-meta">Darren Elsby (CEO &amp; Founder)</div>
  <div class="abs stars">★★★★★</div>
  <p class="abs t-quote">Lorem Ipsum is simply dummy text of the printing and typesetting industry. Lorem Ipsum has been the industry's standard dummy text ever since the 1500s, when an unknown printer took a galley of type and scrambled it to make a type specimen book. It has survived not only five centuries.</p>
  <div class="abs dots"><i class="on"></i><i></i><i></i><i></i></div>

  <h2 class="abs v-title">Our Company Values</h2>
  <div class="abs small-rule" style="left:505px;top:1722px"></div>
  <div class="abs tabs"><div class="on">Quality</div><div>Commitment</div><div>Success</div></div>
  <div class="abs v-sub">Our Company Quality</div>
  <p class="abs v-text">Lorem Ipsum is simply dummy text of the printing and typesetting industry. Lorem Ipsum has been the industry's standard dummy text ever since the 1500s, when an unknown printer took a galley of type and scrambled it to make a type specimen book. It has survived not only five centuries.</p>
  <div class="abs v-device" role="img" aria-label="Laptop and documents on a desk"></div>
  <ul class="abs checklist" style="left:505px;top:1960px">
    <li><svg class="tick" viewBox="0 0 10 10"><path d="M1 5l3 3 5-6" fill="none" stroke="#f37122" stroke-width="2"/></svg>Our Company Growth</li>
    <li><svg class="tick" viewBox="0 0 10 10"><path d="M1 5l3 3 5-6" fill="none" stroke="#f37122" stroke-width="2"/></svg>2000 Employed</li>
    <li><svg class="tick" viewBox="0 0 10 10"><path d="M1 5l3 3 5-6" fill="none" stroke="#f37122" stroke-width="2"/></svg>Customer Relationship</li>
  </ul>
  <ul class="abs checklist" style="left:690px;top:1960px">
    <li><svg class="tick" viewBox="0 0 10 10"><path d="M1 5l3 3 5-6" fill="none" stroke="#f37122" stroke-width="2"/></svg>Our Company Growth</li>
    <li><svg class="tick" viewBox="0 0 10 10"><path d="M1 5l3 3 5-6" fill="none" stroke="#f37122" stroke-width="2"/></svg>2000 Employed</li>
    <li><svg class="tick" viewBox="0 0 10 10"><path d="M1 5l3 3 5-6" fill="none" stroke="#f37122" stroke-width="2"/></svg>Customer Relationship</li>
  </ul>
</section>

<section>
  <div class="abs help-band"></div>
  <div class="abs help-photo" role="img" aria-label="Smiling businessman leaning forward at a desk"></div>
  <div class="abs help-frame"></div>
  <h2 class="abs help-title">WE HELAPING SMALL BUSINESS</h2>
  <p class="abs help-text">Lorem Ipsum is simply dummy text of the printing and typesetting industry. Lorem Ipsum has been the industry's standard dummy text ever since the 1500s, when an unknown printer took a galley of type and scrambled it to make a type specimen book. It has survived not only five centuries.</p>
  <ul class="abs checklist help-list" style="left:583px;top:2290px">
    <li><svg class="tick" viewBox="0 0 10 10"><path d="M1 5l3 3 5-6" fill="none" stroke="#f37122" stroke-width="2"/></svg>Audit &amp; Assurance</li>
    <li><svg class="tick" viewBox="0 0 10 10"><path d="M1 5l3 3 5-6" fill="none" stroke="#f37122" stroke-width="2"/></svg>Business Services</li>
    <li><svg class="tick" viewBox="0 0 10 10"><path d="M1 5l3 3 5-6" fill="none" stroke="#f37122" stroke-width="2"/></svg>IT Control Solutions</li>
  </ul>
  <ul class="abs checklist help-list" style="left:850px;top:2290px">
    <li><svg class="tick" viewBox="0 0 10 10"><path d="M1 5l3 3 5-6" fill="none" stroke="#f37122" stroke-width="2"/></svg>Tax Advisory Services</li>
    <li><svg class="tick" viewBox="0 0 10 10"><path d="M1 5l3 3 5-6" fill="none" stroke="#f37122" stroke-width="2"/></svg>Year End Tax Planning</li>
    <li><svg class="tick" viewBox="0 0 10 10"><path d="M1 5l3 3 5-6" fill="none" stroke="#f37122" stroke-width="2"/></svg>Financial Planning</li>
  </ul>
</section>

<section class="abs stats">
  <div class="stat" style="left:186px"><b>12</b><span>Years of<br>Experiences</span></div>
  <div class="stat" style="left:400px"><b>54</b><span>Professional<br>Advisors</span></div>
  <div class="stat" style="left:650px"><b>40</b><span>News Cases<br>Every Years</span></div>
  <div class="stat" style="left:940px"><b>89</b></div>
</section>

<section>
  <h2 class="section-title team-title">Our Amazing Team</h2>
  <div class="abs team">
    <div><div class="member-photo" role="img" aria-label="Portrait of a smiling female advisor" style="background:linear-gradient(160deg,#e7dcd0,#b9a796)"></div><div class="member-tag"><h4>SAM DORLEY</h4><p>INSURANCE ADVISOR</p></div></div>
    <div><div class="member-photo" role="img" aria-label="Portrait of a male advisor" style="background:linear-gradient(160deg,#dfe3e8,#8e98a4)"></div><div class="member-tag"><h4>SAM DORLEY</h4><p>INSURANCE ADVISOR</p></div></div>
    <div><div class="member-photo" role="img" aria-label="Portrait of a senior male advisor" style="background:linear-gradient(160deg,#e4e4e4,#8c8c8c)"></div><div class="member-tag"><h4>SAM DORLEY</h4><p>INSURANCE ADVISOR</p></div></div>
    <div><div class="member-photo" role="img" aria-label="Portrait of a senior female advisor" style="background:linear-gradient(160deg,#eeeeee,#a9a29b)"></div><div class="member-tag"><h4>SAM DORLEY</h4><p>INSURANCE ADVISOR</p></div></div>
  </div>
</section>

<section class="abs cta">
  <p>If you have any query for related investment ... We are available</p>
  <div class="abs btn-cta">CONTACT US <i></i></div>
</section>

<section class="abs contact">
  <h2>Contact us</h2>
</section>
<div class="abs contact-map" role="img" aria-label="Faint world map in the background"></div>
<div class="field" style="top:3355px">First Name</div>
<div class="field" style="top:3430px">Email Address</div>
<div class="field" style="top:3505px">Subject</div>
<div class="field area">Description</div>
<a class="abs btn send">Send Message</a>

<footer class="abs footer">
  <p>Copyright © 2016. All rights reserved. www.brellomint.com.au</p>
  <div class="abs fsocial"><i></i><i></i><i></i><i></i></div>
</footer>

</body>
</html>
```